Store Signage for New Location

I need a banner for my new location. It needs to communicate 1: our name, 2: our phone number 3: our message. This is going to be a 7 foot wide banner that is 4 feet tall. It needs to be a very high resolution design so it prints properly.

Our phone number is (555) 418-2097

Our Message: The HONEST alternative to the dealer.

Or: Your Honest Auto Service Center

"Honest" is our key word here.
Updates

Target Market(s)

Drive-by traffic.

Industry/Entity Type

Auto Repair

Requirements
Must have
• The name of our business: Fair Lane Auto Repair
• Our phone number: (555) 418-2097
• Our message: The HONEST alternative to the dealership.
• or: Your Honest Service Center
Nice to have
• I really just need a clean layout using the uploaded logo and font. It needs to be highly visible as a sign that is seen by drive-by traffic.
• I'd like the color scheme to be the same as what I have, however, you're more than welcome to add detail and color as needed.

```html
<!DOCTYPE html>
<html lang="en">
<head>
<meta charset="utf-8">
<title>Fair Lane Auto Repair – Store Banner</title>
<link rel="stylesheet" href="https://fonts.googleapis.com/css2?family=League+Spartan:wght@600;700&display=swap">
<style>
  :root {
    --orange: #f37329;
    --orange-deep: #cb5f29;
    --ink: #0a0a0a;
    --paper: #ffffff;
  }
  html, body {
    margin: 0;
    padding: 0;
    overflow: hidden;
    background: var(--paper);
  }
  .banner {
    position: relative;
    width: 1200px;
    height: 686px;
    overflow: hidden;
    background: var(--paper);
    font-family: "League Spartan", "Futura", sans-serif;
  }
  .accent-band {
    position: absolute;
    inset: 0;
    width: 1200px;
    height: 686px;
  }
  .brand-mark {
    position: absolute;
    left: 52px;
    top: 58px;
    display: flex;
    align-items: center;
    gap: 12px;
  }
  .brand-mark__dot {
    width: 40px;
    height: 40px;
    border-radius: 50%;
    background: var(--ink);
  }
  .brand-mark__name {
    font-weight: 700;
    font-size: 20px;
    color: var(--ink);
    line-height: 1;
  }
  .business-name {
    position: absolute;
    left: 0;
    right: 0;
    top: 196px;
    margin: 0;
    text-align: center;
    font-weight: 700;
    font-size: 94px;
    line-height: 100px;
    letter-spacing: 0.06em;
    color: var(--ink);
  }
  .tagline {
    position: absolute;
    left: 0;
    right: 0;
    top: 426px;
    height: 78px;
    display: flex;
    justify-content: center;
    align-items: center;
    gap: 24px;
    margin: 0;
    font-weight: 700;
    font-size: 58px;
    letter-spacing: 0.02em;
    color: var(--orange);
    white-space: nowrap;
  }
  .tagline__key {
    display: inline-block;
    background: var(--orange);
    color: var(--paper);
    border-radius: 13px;
    padding: 12px 12px 6px;
    line-height: 1;
  }
  .phone {
    position: absolute;
    right: 56px;
    top: 586px;
    margin: 0;
    font-weight: 700;
    font-size: 62px;
    line-height: 1;
    letter-spacing: 0.03em;
    color: var(--ink);
  }
</style>
</head>
<body>
  <main class="banner">
    <svg class="accent-band" viewBox="0 0 1200 686" role="img" aria-label="Orange accent bands sweeping across the top right and bottom of the banner">
      <defs>
        <linearGradient id="band-top" x1="0" y1="0" x2="1" y2="1">
          <stop offset="0" stop-color="var(--orange)"/>
          <stop offset="1" stop-color="var(--orange-deep)"/>
        </linearGradient>
        <linearGradient id="band-bottom" x1="0" y1="0" x2="1" y2="0">
          <stop offset="0" stop-color="var(--orange-deep)"/>
          <stop offset="1" stop-color="var(--orange)"/>
        </linearGradient>
      </defs>
      <path fill="url(#band-top)" d="M340,0 L1200,0 L1200,200 C960,100 660,30 340,0 Z"/>
      <path fill="url(#band-bottom)" d="M0,485 C340,612 720,666 1200,682 L1200,686 L0,686 Z"/>
    </svg>

    <div class="brand-mark">
      <span class="brand-mark__dot"></span>
      <span class="brand-mark__name">Fair Lane Auto Repair</span>
    </div>

    <h1 class="business-name">Fair Lane<br>Auto Repair</h1>

    <p class="tagline">
      <span>YOUR</span>
      <span class="tagline__key">HONEST</span>
      <span>AUTO SERVICE CENTER</span>
    </p>

    <p class="phone">(555) 418-2097</p>
  </main>
</body>
</html>
```